TEFL Internship Page Redesign

Hi guys! I have put together a design brief in this document - https://files.plimworth.net/sheet/d/7kq2Zx_P-4bwTrNmL9x83vHcYsW0qE5dJfAaB21tuu/view. I have made sure to give access.

Please read carefully and elevate the current design on the link provided. I have tried to give some much specifics as possible. Where I haven't please use your judgement to come with something. For all text please use "poppins".

```html
<!DOCTYPE html>
<html lang="en">
<head>
<meta charset="utf-8">
<title>TEFL Internships | Lumen TEFL</title>
<link href="https://fonts.googleapis.com/css2?family=Poppins:wght@300;400;500;600;700;800&family=Kaushan+Script&display=swap" rel="stylesheet">
<style>
:root{
  --teal:#14b1ba;
  --teal-dark:#0e9aa3;
  --navy:#1d3a5c;
  --orange:#f0a03a;
  --green:#2b8a61;
  --blue:#5d7fd0;
  --salmon:#df7d66;
  --ink:#222;
  --grey:#666;
  --line:#e2e2e2;
  --mint:#eefafb;
  --peach:#fcf1e4;
  --white:#fff;
}
*{box-sizing:border-box;margin:0;padding:0}
html,body{width:1200px;height:5329px;overflow:hidden}
body{font-family:"Poppins",sans-serif;color:var(--ink);background:var(--white);position:relative}
section,header,footer{position:absolute;left:0;width:1200px}
a{color:inherit;text-decoration:none}

/* hero */
.hero{top:0;height:642px;background:linear-gradient(180deg,#3f6a4a 0%,#5c8f6a 30%,#7fb6c4 55%,#4f8fa6 75%,#6c5a3f 100%)}
.nav{position:absolute;top:0;left:0;width:1200px;height:90px}
.brand{position:absolute;left:112px;top:20px;color:var(--white);font-weight:700;font-size:26px;display:flex;align-items:center;gap:8px}
.brand i{display:block;width:14px;height:14px;background:var(--white)}
.menu{position:absolute;left:310px;top:56px;display:flex;gap:30px;color:var(--white);font-size:13px}
.search{position:absolute;left:770px;top:16px;width:207px;height:32px;border:1px solid var(--white);border-radius:3px;color:var(--white);font-size:12px;padding:7px 12px}
.search svg{position:absolute;right:8px;top:8px}
.demo{position:absolute;left:989px;top:14px;width:98px;height:34px;background:var(--teal);color:var(--white);font-size:11px;font-weight:700;display:flex;align-items:center;justify-content:center}
.hero h1{position:absolute;top:252px;width:100%;text-align:center;color:var(--white);font-size:72px;font-weight:700;letter-spacing:-1px}
.tagline{position:absolute;top:336px;width:100%;text-align:center;color:var(--white);font-family:"Kaushan Script",cursive;font-size:52px}
.band{top:642px;height:61px;background:var(--navy);color:var(--white);font-size:13px;text-align:center;line-height:61px}
.band a{color:var(--teal);text-decoration:underline;font-weight:600}

.section-title{position:absolute;width:100%;text-align:center;color:var(--teal);font-weight:700;font-size:40px}

/* internship cards */
.cards{top:703px;height:1540px}
.card-grid{position:absolute;left:112px;top:182px;display:grid;grid-template-columns:repeat(4,232px);grid-auto-rows:604px;gap:16px}
.card{border:1px solid var(--line);background:var(--white);display:flex;flex-direction:column}
.card .photo{height:155px}
.card .body{padding:16px 18px}
.price{color:var(--teal);font-weight:600;font-size:17px;display:flex;align-items:center;gap:8px}
.meta{font-size:11.5px;color:var(--grey);display:flex;align-items:center;gap:10px;margin-top:8px}
.badge{display:inline-block;margin:18px 0 14px;background:var(--teal);color:var(--white);font-size:11px;font-weight:700;padding:8px 16px}
.card ul{list-style:none}
.card li{font-size:11.5px;color:var(--grey);line-height:21px;padding-left:14px;position:relative;margin-bottom:21px}
.card li::before{content:"";position:absolute;left:0;top:8px;width:5px;height:5px;border-radius:50%;background:var(--orange)}
.links{display:flex;gap:22px;font-size:11px;font-weight:700;padding-left:18px}
.links .more{color:var(--teal);border-bottom:1px solid var(--teal)}
.links .apply{color:var(--orange);border-bottom:1px solid var(--orange)}

/* intro + faq */
.intro{top:2265px;height:622px}
.intro .left{position:absolute;left:0;top:0;width:597px;height:622px;background:var(--mint);text-align:center}
.intro .right{position:absolute;left:597px;top:0;width:603px;height:622px;background:var(--peach)}
.intro h2{color:var(--teal);font-size:38px;font-weight:700;margin-top:62px}
.intro .lead{color:var(--orange);font-size:13.5px;line-height:25px;width:460px;margin:16px auto 0}
.intro .copy{font-size:13.5px;color:var(--grey);line-height:28px;width:488px;margin:20px auto 0;text-align:justify;text-align-last:center}
.faq h2{color:var(--teal);font-size:30px;font-weight:700;text-align:center;margin-top:62px}
.faq-list{position:absolute;left:65px;top:134px;width:470px}
.faq-item{background:var(--white);margin-bottom:20px;padding:0 18px;box-shadow:0 1px 4px rgba(0,0,0,.05)}
.faq-q{height:52px;display:flex;align-items:center;justify-content:space-between;font-size:13.5px;color:var(--grey)}
.faq-item.open .faq-q{color:var(--ink);font-weight:500;border-bottom:1px solid var(--line)}
.toggle{width:28px;height:28px;background:#eee;color:var(--grey);font-size:14px;display:flex;align-items:center;justify-content:center}
.faq-a{font-size:11.5px;color:var(--grey);line-height:22px;padding:18px 0 20px}

/* how it works */
.how{top:2887px;height:506px}
.how .section-title{top:80px}
.steps{position:absolute;left:112px;top:206px;display:grid;grid-template-columns:repeat(4,232px);gap:16px}
.step{height:203px;position:relative;color:var(--white);display:flex;flex-direction:column;align-items:center;justify-content:flex-end;padding-bottom:36px;font-size:20px;font-weight:700}
.step svg{margin-bottom:14px}
.num{position:absolute;top:-20px;left:96px;width:40px;height:40px;border-radius:50%;background:var(--white);border:3px solid currentColor;font-size:18px;display:flex;align-items:center;justify-content:center}
.s1{background:var(--teal)}.s1 .num{color:var(--teal)}
.s2{background:var(--green)}.s2 .num{color:var(--green)}
.s3{background:var(--blue)}.s3 .num{color:var(--blue)}
.s4{background:var(--salmon)}.s4 .num{color:var(--salmon)}

/* contact + guide */
.cta{top:3393px;height:405px}
.cta .panel{position:absolute;top:0;width:600px;height:405px;text-align:center}
.cta .mint{left:0;background:var(--mint)}
.cta .peach{left:600px;background:var(--peach)}
.icon-ring{width:72px;height:72px;border-radius:50%;background:var(--white);margin:48px auto 0;display:flex;align-items:center;justify-content:center}
.cta h2{color:var(--teal);font-size:31px;font-weight:700;margin-top:16px}
.cta p{font-size:12.5px;color:var(--grey);line-height:26px;width:510px;margin:12px auto 0}
.btn{display:inline-block;margin-top:26px;color:var(--white);font-size:11px;font-weight:700;padding:12px 22px}
.btn.teal{background:var(--teal)}
.btn.orange{background:var(--orange)}

/* articles */
.articles{top:3798px;height:888px}
.articles h2{position:absolute;left:112px;top:86px;color:var(--teal);font-size:40px;font-weight:700}
.view-all{position:absolute;left:949px;top:98px;width:139px;height:36px;background:var(--teal);color:var(--white);font-size:14px;font-weight:600;display:flex;align-items:center;justify-content:center}
.post-grid{position:absolute;left:112px;top:160px;display:grid;grid-template-columns:repeat(3,310px);grid-auto-rows:327px;gap:16px 23px}
.post .photo{height:195px}
.post .caption{background:var(--white);width:278px;margin:-26px 0 0 24px;position:relative;padding:10px 8px 0}
.kicker{font-size:14px;color:var(--grey)}
.post h3{font-size:20px;font-weight:700;line-height:26px;margin-top:8px}
.post-meta{display:flex;gap:32px;font-size:11.5px;color:var(--grey);margin-top:16px;padding-left:8px}
.post-meta span{display:flex;align-items:center;gap:5px}

/* footer */
.footer{top:4686px;height:424px;background:var(--teal);color:var(--white)}
.footer .brand-foot{position:absolute;left:0;top:58px;width:100%;text-align:center;font-weight:700;font-size:28px}
.foot-cols{position:absolute;left:265px;top:154px;display:flex;gap:22px;text-align:center}
.foot-col{width:112px}
.foot-col h4{font-size:11px;font-weight:700;line-height:14px;margin-bottom:10px}
.foot-col li{list-style:none;font-size:9px;line-height:13px;margin-bottom:10px}
.strip{top:5110px;height:155px;background:linear-gradient(90deg,#2f7fa0 0%,#4aa1b5 30%,#6a8a5e 55%,#c9a97a 75%,#3d7c9a 100%)}
.strip-info{position:absolute;width:100%;top:38px;text-align:center;color:var(--white);font-size:9px;line-height:20px}
.pay{position:absolute;left:18px;top:105px;display:flex;gap:12px}
.pay span{width:34px;height:22px;background:var(--white);border-radius:3px}
.social{position:absolute;right:22px;top:100px;display:flex;gap:10px}
.social span{width:24px;height:24px;border-radius:50%;background:var(--white)}
.copyright{top:5265px;height:64px;font-size:11px;color:var(--grey);text-align:center;line-height:64px}
.copyright em{position:absolute;right:42px;font-style:normal}
</style>
</head>
<body>

<header class="hero">
  <div role="img" aria-label="Photo of long-tail boats moored in a turquoise bay beneath forested limestone cliffs" style="position:absolute;inset:0"></div>
  <nav class="nav">
    <a class="brand" href="#"><i></i>Lumen TEFL</a>
    <div class="menu"><span>Why Lumen? ⌄</span><span>TEFL Courses ⌄</span><span>Teach English Online ⌄</span><span>Teaching Opportunities ⌄</span><span>Jobs</span><span>Blog</span><span>Support ⌄</span></div>
    <div class="search">Search<svg width="14" height="14" viewBox="0 0 14 14"><circle cx="6" cy="6" r="4.5" fill="none" stroke="#fff" stroke-width="1.6"/><path d="M9.5 9.5L13 13" stroke="#fff" stroke-width="1.6"/></svg></div>
    <a class="demo" href="#">DEMO ME</a>
  </nav>
  <h1>TEFL Internships</h1>
  <div class="tagline">Teach Enrich Empower</div>
</header>
<section class="band">Join a global community of over 200,000 TEFL teachers working throughout the world! <a href="#">Enrol me!</a></section>

<section class="cards">
  <div class="section-title" style="top:90px">Internship cards</div>
  <div class="card-grid">
    <article class="card"><div class="photo" role="img" aria-label="Students walking along a city street" style="background:linear-gradient(160deg,#9a8d7c,#5f6b63)"></div><div class="body"><div class="price">▭ £699GBP</div><div class="meta">▦ February &amp; July</div><div class="meta">▰ $600 – $1,200 per month</div><span class="badge">BENEFITS:</span><ul><li>A monthly stipend of $600 – $1,200</li><li>Airport transfer upon arrival in Buenos Aires free transfer to host town/city</li><li>Home-stay accommodation with an Argentine host family</li><li>4 hours of one-to-one Spanish lessons weekly</li></ul></div><div class="links"><a class="more" href="#">MORE INFO</a><a class="apply" href="#">APPLY NOW</a></div></article>
    <article class="card"><div class="photo" role="img" aria-label="Paper lantern glowing at night" style="background:radial-gradient(circle at 50% 40%,#e8d6a8,#2a2622 60%)"></div><div class="body"><div class="price">▭ No fee</div><div class="meta">▦ February &amp; July</div><div class="meta">▰ $600 – $1,200 per month</div><span class="badge">BENEFITS:</span><ul><li>A monthly stipend of $600 – $1,200</li><li>Airport transfer upon arrival in Buenos Aires free transfer to host town/city</li><li>Home-stay accommodation with an Argentine host family</li><li>4 hours of one-to-one Spanish lessons weekly</li></ul></div><div class="links"><a class="more" href="#">MORE INFO</a><a class="apply" href="#">APPLY NOW</a></div></article>
    <article class="card"><div class="photo" role="img" aria-label="City skyline at dusk over a river" style="background:linear-gradient(180deg,#8fa8d8,#c9a7c4 55%,#3b4d7a)"></div><div class="body"><div class="price">▭ No fee</div><div class="meta">▦ February &amp; July</div><div class="meta">▰ $600 – $1,200 per month</div><span class="badge">BENEFITS:</span><ul><li>A monthly stipend of $600 – $1,200</li><li>Airport transfer upon arrival in Buenos Aires free transfer to host town/city</li><li>Home-stay accommodation with an Argentine host family</li><li>4 hours of one-to-one Spanish lessons weekly</li></ul></div><div class="links"><a class="more" href="#">MORE INFO</a><a class="apply" href="#">APPLY NOW</a></div></article>
    <article class="card"><div class="photo" role="img" aria-label="Neon-lit shop fronts on a night street" style="background:linear-gradient(180deg,#1f4f7a,#2a8c9c 60%,#163049)"></div><div class="body"><div class="price">▭ No fee</div><div class="meta">▦ February &amp; July</div><div class="meta">▰ $600 – $1,200 per month</div><span class="badge">BENEFITS:</span><ul><li>A monthly stipend of $600 – $1,200</li><li>Airport transfer upon arrival in Buenos Aires free transfer to host town/city</li><li>Home-stay accommodation with an Argentine host family</li><li>4 hours of one-to-one Spanish lessons weekly</li></ul></div><div class="links"><a class="more" href="#">MORE INFO</a><a class="apply" href="#">APPLY NOW</a></div></article>
    <article class="card"><div class="photo" role="img" aria-label="Colourful mosaic terrace overlooking a city" style="background:linear-gradient(180deg,#5b8fd0,#c7a06a 60%,#7a5d3b)"></div><div class="body"><div class="price">▭ No fee</div><div class="meta">▦ February &amp; July</div><div class="meta">▰ $600 – $1,200 per month</div><span class="badge">BENEFITS:</span><ul><li>A monthly stipend of $600 – $1,200</li><li>Airport transfer upon arrival in Buenos Aires free transfer to host town/city</li><li>Home-stay accommodation with an Argentine host family</li><li>4 hours of one-to-one Spanish lessons weekly</li></ul></div><div class="links"><a class="more" href="#">MORE INFO</a><a class="apply" href="#">APPLY NOW</a></div></article>
    <article class="card"><div class="photo" role="img" aria-label="Red and green temple roofs" style="background:linear-gradient(180deg,#6a9c86,#b8423a 60%,#7a2a22)"></div><div class="body"><div class="price">▭ No fee</div><div class="meta">▦ February &amp; July</div><div class="meta">▰ $600 – $1,200 per month</div><span class="badge">BENEFITS:</span><ul><li>A monthly stipend of $600 – $1,200</li><li>Airport transfer upon arrival in Buenos Aires free transfer to host town/city</li><li>Home-stay accommodation with an Argentine host family</li><li>4 hours of one-to-one Spanish lessons weekly</li></ul></div><div class="links"><a class="more" href="#">MORE INFO</a><a class="apply" href="#">APPLY NOW</a></div></article>
    <article class="card"><div class="photo" role="img" aria-label="Hilltop church above a city at sunset" style="background:linear-gradient(180deg,#d9965a,#a85d3c 55%,#3e2b2a)"></div><div class="body"><div class="price">▭ No fee</div><div class="meta">▦ February &amp; July</div><div class="meta">▰ $600 – $1,200 per month</div><span class="badge">BENEFITS:</span><ul><li>A monthly stipend of $600 – $1,200</li><li>Airport transfer upon arrival in Buenos Aires free transfer to host town/city</li><li>Home-stay accommodation with an Argentine host family</li><li>4 hours of one-to-one Spanish lessons weekly</li></ul></div><div class="links"><a class="more" href="#">MORE INFO</a><a class="apply" href="#">APPLY NOW</a></div></article>
    <article class="card"><div class="photo" role="img" aria-label="Blue-painted alley with stone steps" style="background:linear-gradient(160deg,#2f5fa8,#4f86c6 60%,#23477e)"></div><div class="body"><div class="price">▭ No fee</div><div class="meta">▦ February &amp; July</div><div class="meta">▰ $600 – $1,200 per month</div><span class="badge">BENEFITS:</span><ul><li>A monthly stipend of $600 – $1,200</li><li>Airport transfer upon arrival in Buenos Aires free transfer to host town/city</li><li>Home-stay accommodation with an Argentine host family</li><li>4 hours of one-to-one Spanish lessons weekly</li></ul></div><div class="links"><a class="more" href="#">MORE INFO</a><a class="apply" href="#">APPLY NOW</a></div></article>
  </div>
</section>

<section class="intro">
  <div class="left">
    <h2>TEFL Internships</h2>
    <p class="lead">Our TEFL internships are a great way to start your new career. Get paid a great salary and receive support throughout your contract!</p>
    <p class="copy">Our TEFL internships are open to anyone who has enrolled on the Level 3 or Level 5 version of our TEFL course and meets the requirements listed for each opportunity. Our TEFL internships are the fastest way to kick start your TEFL career whilst receiving a higher level of support than standard TEFL jobs. Most of our TEFL internships will include 24×7 local support, an orientation week with lots of other foreign teachers, accommodation, living allowance, help getting a bank account and sim card, and fewer working hours than a standard contracted teacher. Our TEFL internships are the perfect way to bridge the gap between qualifying and starting a more formal teaching role.</p>
  </div>
  <div class="right faq">
    <h2>Frequently Asked Questions</h2>
    <div class="faq-list">
      <div class="faq-item open"><div class="faq-q">Lorem ipsum dolor sit amet, consectetur adipisc <span class="toggle">–</span></div><p class="faq-a">Lorem ipsum dolor sit amet, consectetur adipiscing elit, sed do eiusmod tempor incididunt ut labore et dolore magna aliqua. Ut enim ad minim veniam, quis nostrud exercitation ullamco laboris nisi ut aliquip ex ea commodo consequat. Lorem ipsum dolor sit amet, consectetur adipisci ng elit, sed do eiusmod tempor incididunt</p></div>
      <div class="faq-item"><div class="faq-q">Lorem ipsum dolor sit amet, consectetur adipisc <span class="toggle">+</span></div></div>
      <div class="faq-item"><div class="faq-q">Lorem ipsum dolor sit amet, consectetur adipisc <span class="toggle">+</span></div></div>
      <div class="faq-item"><div class="faq-q">Lorem ipsum dolor sit amet, consectetur adipisc <span class="toggle">+</span></div></div>
    </div>
  </div>
</section>

<section class="how">
  <div class="section-title">How it Works</div>
  <div class="steps">
    <div class="step s1"><span class="num">01</span><svg width="70" height="66" viewBox="0 0 70 66" fill="none" stroke="#fff" stroke-width="4"><rect x="6" y="4" width="36" height="50" rx="3"/><path d="M14 16h4M24 16h12M14 28h4M24 28h12M14 40h4M24 40h6"/><circle cx="52" cy="48" r="13" fill="#fff"/><path d="M45 48l5 5 9-10" stroke="#14b1ba"/></svg>Apply</div>
    <div class="step s2"><span class="num">02</span><svg width="80" height="66" viewBox="0 0 80 66" fill="#fff"><circle cx="18" cy="12" r="9"/><path d="M4 40a14 14 0 0 1 28 0v6H4z"/><rect x="40" y="4" width="30" height="16" rx="2"/><circle cx="58" cy="32" r="8"/><path d="M44 58a14 14 0 0 1 28 0v6H44z"/><rect x="2" y="50" width="36" height="6"/></svg>Interview</div>
    <div class="step s3"><span class="num">03</span><svg width="66" height="66" viewBox="0 0 66 66" fill="none" stroke="#fff" stroke-width="4"><path d="M14 4h26l12 12v42H14z"/><path d="M22 24h22M22 34h22M22 44h14"/><circle cx="20" cy="50" r="11" fill="#fff"/><path d="M14 50l4 4 8-8" stroke="#5d7fd0"/></svg>Document</div>
    <div class="step s4"><span class="num">04</span><svg width="80" height="66" viewBox="0 0 80 66" fill="#fff"><rect x="30" y="2" width="46" height="32" fill="none" stroke="#fff" stroke-width="4"/><circle cx="20" cy="12" r="8"/><path d="M8 44a12 12 0 0 1 24 0v6H8z"/><circle cx="14" cy="52" r="5"/><circle cx="36" cy="52" r="5"/><circle cx="58" cy="52" r="5"/><rect x="4" y="58" width="68" height="6"/></svg>Teach</div>
  </div>
</section>

<section class="cta">
  <div class="panel mint">
    <div class="icon-ring"><svg width="34" height="34" viewBox="0 0 34 34" fill="none" stroke="#14b1ba" stroke-width="2"><rect x="4" y="3" width="16" height="28" rx="2"/><path d="M10 27h4"/><path d="M22 10c4 0 7 3 7 7M22 5c7 0 11 5 11 12"/></svg></div>
    <h2>Quick Contact</h2>
    <p>Lorem ipsum dolor sit amet, consectetur adipiscing elit, sed do eiusmod tempor incididunt ut labore et dolore magna aliqua. Ut enim ad minim veniam, quis nostrud exercitation ullamco labor nisi ut aliquip ex ea commodo consequat.</p>
    <a class="btn teal" href="#">CALL NOW</a>
  </div>
  <div class="panel peach">
    <div class="icon-ring"><svg width="36" height="34" viewBox="0 0 36 34" fill="none" stroke="#14b1ba" stroke-width="2"><rect x="3" y="5" width="30" height="20" rx="2"/><path d="M12 31h12M18 25v6"/><circle cx="18" cy="15" r="5"/><path d="M18 2v3M8 4l2 2M28 4l-2 2"/></svg></div>
    <h2>TEFL Guide</h2>
    <p>Lorem ipsum dolor sit amet, consectetur adipiscing elit, sed do eiusmod tempor incididunt ut labore et dolore magna aliqua. Ut enim ad minim veniam, quis nostrud exercitation ullamco labor nisi ut aliquip ex ea commodo consequat.</p>
    <a class="btn orange" href="#">DOWNLOAD NOW</a>
  </div>
</section>

<section class="articles">
  <h2>Internship Articles</h2>
  <a class="view-all" href="#">View All</a>
  <div class="post-grid">
    <article class="post"><div class="photo" role="img" aria-label="Traveller relaxing among tropical plants" style="background:linear-gradient(160deg,#4f7a3a,#8fae5e 50%,#3a5a2e)"></div><div class="caption"><div class="kicker">Duis aute irure dolor</div><h3>Lorem ipsum dolor sit amet, consectetur</h3></div><div class="post-meta"><span>👤 Mira Dalton Vance</span><span>▦ Mar 13, 2023</span></div></article>
    <article class="post"><div class="photo" role="img" aria-label="Hiker sitting on a cliff above a misty valley at sunrise" style="background:linear-gradient(180deg,#e7c08a,#9fb0a4 45%,#3e5e3a)"></div><div class="caption"><div class="kicker">Duis aute irure dolor</div><h3>Lorem ipsum dolor sit amet, consectetur</h3></div><div class="post-meta"><span>👤 Mira Dalton Vance</span><span>▦ Mar 13, 2023</span></div></article>
    <article class="post"><div class="photo" role="img" aria-label="Rocky shoreline with tide pools" style="background:linear-gradient(180deg,#c7d5dc,#7f8f8e 55%,#4b4a3e)"></div><div class="caption"><div class="kicker">Duis aute irure dolor</div><h3>Lorem ipsum dolor sit amet, consectetur</h3></div><div class="post-meta"><span>👤 Mira Dalton Vance</span><span>▦ Mar 13, 2023</span></div></article>
    <article class="post"><div class="photo" role="img" aria-label="Traveller resting in a hammock in sunlit greenery" style="background:linear-gradient(160deg,#d9c25a,#9db04a 50%,#5a7a2e)"></div><div class="caption"><div class="kicker">Duis aute irure dolor</div><h3>Lorem ipsum dolor sit amet, consectetur</h3></div><div class="post-meta"><span>👤 Mira Dalton Vance</span><span>▦ Mar 13, 2023</span></div></article>
    <article class="post"><div class="photo" role="img" aria-label="Coastal town and turquoise harbour from above" style="background:linear-gradient(180deg,#b9d3e2,#3fa7b5 55%,#4b7a4c)"></div><div class="caption"><div class="kicker">Duis aute irure dolor</div><h3>Lorem ipsum dolor sit amet, consectetur</h3></div><div class="post-meta"><span>👤 Mira Dalton Vance</span><span>▦ Mar 13, 2023</span></div></article>
    <article class="post"><div class="photo" role="img" aria-label="Hiker with backpack on green hills" style="background:linear-gradient(180deg,#a9bfc7,#5f8a4e 50%,#3b5a2c)"></div><div class="caption"><div class="kicker">Duis aute irure dolor</div><h3>Lorem ipsum dolor sit amet, consectetur</h3></div><div class="post-meta"><span>👤 Mira Dalton Vance</span><span>▦ Mar 13, 2023</span></div></article>
  </div>
</section>

<footer class="footer">
  <div class="brand-foot">Lumen TEFL</div>
  <div class="foot-cols">
    <div class="foot-col"><h4>Why Lumen?</h4><ul><li>Why Choose Us?</li><li>Charity Partnership</li><li>Accreditation</li><li>Compare TEFL Course Providers</li><li>Meet our Alumni</li><li>Meet our Trainers</li><li>Company profile</li><li>Testimonials</li><li>Affiliate Programme</li></ul></div>
    <div class="foot-col"><h4>TEFL Courses</h4><ul><li>View All TEFL Courses</li><li>Online TEFL Course (Level 3 – 120hrs)</li><li>Online TEFL Course (Level 5 – 168hrs)</li><li>Observed Teaching Practice Course (Level 5)</li><li>TEFL Top-Up Courses</li></ul></div>
    <div class="foot-col"><h4>Teaching Opportunities</h4><ul><li>TEFL Jobs</li><li>TEFL Internships</li><li>TEFL Volunteering</li><li>Country Profiles</li><li>Teaching Without a Degree</li></ul></div>
    <div class="foot-col"><h4>Student Support Centre</h4><ul><li>TEFL Learning Centre</li><li>Frequently Asked Questions</li></ul></div>
    <div class="foot-col"><h4>Talk to Us</h4><ul><li>Get in Touch</li><li>Request Call Back</li><li>Blog</li></ul></div>
  </div>
</footer>
<section class="strip" role="img" aria-label="Beach and sea scene behind footer details">
  <div class="strip-info"><strong>Call us for help +1 555 014 2290</strong><br>Lumen TEFL, 12 Harbour Row, Suite 4, Portwell, PW 20418<br>Terms and Conditions · Privacy Policy</div>
  <div class="pay"><span></span><span></span><span></span><span></span><span></span><span></span></div>
  <div class="social"><span></span><span></span><span></span><span></span><span></span><span></span></div>
</section>
<section class="copyright">© Copyrights 2023 Company Name | All Rights Reserved<em>C38</em></section>

</body>
</html>
```